Redesign, cleanup and edit my Presentations

I have a series of power points that I use for training purposes. They were made by me over time. During the last couple years, I have evolved their look and content over time, but not consistently. More specifically, I have not gone back to re-edit the older decks. So, some decks are too wordy, too long, or and don't look consistent.

I am looking someone who can create a good design that I can use going forward, and who could also apply that theme to the existing decks, along with editing the existing, and future decks, too.

I have a lot of slides to produce and/or edit -approximately 500. But this request is a test to find a powerpoint partner. I am supplying 2 decks. One that's older and more wordy than the other. I would like to see what you would suggest we do differently. So that's what you are bidding on today. Also, you do not have to complete deck "Phase 7.4." I only need enough of the deck done to see where you would take it. Maybe 10 slides? Your choice. However, with that deck, there are lots of opportunities to clarify, re-align, and minimize within that deck.

But, if you are selected, I want to engage with you on an ongoing basis, and send more material your way. Then, you will be engaged to complete all decks.

Please ask me any questions to help you gain a better understanding of this project.

Target Market(s)

People in management, technical, medical, and financial fields who wish to become independent consultants.

Industry/Entity Type

Business Consultant

Font styles to use
Sans Serif

Requirements
Must have
• Use the existing color theme:
• yellow/gold - #f5b300,
• blue - 2b74a6
• Logo doesn't change
• Preferred fonts: Raleway for headings and Open Sans for general text
• Any pictures and graphics should have no copyright restrictions. That is, I should have use of the work without charge.
Nice to have
• I prefer a flat graphic style, although you can use pictures where it conveys a point more effectively.
• Ability to convert the presentations to Google Slides and Apple's Keynote apps.
• Ability to convert presentation to video
Should not have
• Restricted use graphics, photos, or other content.

```html
<!DOCTYPE html>
<html lang="en">
<head>
<meta charset="utf-8">
<title>Your Pitch – Presentation Theme Sheet</title>
<link href="https://fonts.googleapis.com/css2?family=Arimo:wght@400;700&family=Open+Sans:wght@400;600;700;800&family=Raleway:wght@600;700;800&display=swap" rel="stylesheet">
<style>
:root{
  --gold:#f5b300;
  --blue:#2b74a6;
  --slate:#37474f;
  --orange:#f39c33;
  --rust:#e07b1a;
  --ink:#333333;
  --muted:#6b6b6b;
  --sheet:#e8ebef;
  --row:#d9d9d9;
  --white:#ffffff;
}
*{box-sizing:border-box;margin:0;padding:0}
html,body{width:1200px;height:2201px;overflow:hidden;background:var(--sheet)}
body{position:relative;font-family:"Open Sans",sans-serif;color:var(--ink)}

/* hero */
.hero{position:absolute;left:15px;top:51px;width:713px;height:400px;background:var(--gold);box-shadow:3px 4px 6px rgba(0,0,0,.25)}
.hero-title{position:absolute;left:224px;top:160px;font-family:"Arimo",sans-serif;font-weight:700;font-size:70px;color:var(--white);letter-spacing:1px}
.hero-rule{position:absolute;left:227px;top:230px;width:407px;height:1px;background:rgba(255,255,255,.8)}
.hero-sub{position:absolute;left:226px;top:247px;font-size:11px;color:var(--white)}

/* feature checklist */
.features{position:absolute;left:779px;top:0;width:421px;height:470px;font-family:"Open Sans",sans-serif;font-weight:800;font-size:22px;color:#3a3a3a;letter-spacing:.5px}
.features .item{position:absolute;white-space:nowrap}
.features .box{position:absolute;left:0;width:20px;height:20px;border:2.5px solid #3a3a3a;border-radius:2px;box-shadow:2px 2px 2px rgba(0,0,0,.35);background:var(--white)}
.features .sq{position:absolute;left:58px;width:8px;height:8px;background:#3a3a3a}

/* slides */
.slide{position:absolute;width:378px;height:213px;background:var(--white);overflow:hidden;box-shadow:2px 3px 5px rgba(0,0,0,.25)}
.abs{position:absolute}
.brand{position:absolute;top:10px;font-family:"Open Sans",sans-serif;font-weight:700;font-size:7px;color:var(--blue);display:flex;align-items:center;gap:2px}
.brand i{display:inline-block;width:6px;height:6px;border-radius:50%;background:var(--gold)}
.foot{position:absolute;bottom:6px;left:0;width:100%;text-align:center;font-size:5px;color:var(--muted)}
.pageno{position:absolute;bottom:6px;right:26px;font-size:5px;color:var(--muted)}
.heading{position:absolute;font-family:"Raleway",sans-serif;font-weight:700;color:var(--ink);line-height:1.15}
.body{position:absolute;font-size:7px;line-height:1.3;color:var(--ink)}
.photo{position:absolute}
.photo.round{border-radius:50%}
.slide-title{position:absolute;left:20px;top:11px;font-size:8.5px;color:var(--ink)}
.slide-title.strong{font-weight:700}

/* agenda */
.agenda-band{position:absolute;left:0;top:0;width:100%;height:120px;background:var(--gold)}
.agenda-title{position:absolute;top:28px;font-family:"Arimo",sans-serif;font-size:16px;color:var(--white)}
.agenda-label{position:absolute;top:94px;font-size:8px;line-height:1.25;color:var(--white)}
.agenda-label b{font-weight:700}
.agenda-line{position:absolute;top:152px;height:1px;background:#9a9a9a}
.agenda-dot{position:absolute;top:135px;width:34px;height:34px;border-radius:50%;background:var(--gold);display:flex;align-items:center;justify-content:center}

/* statement slide */
.statement{background:var(--slate);color:var(--white);text-align:center}
.statement .lead{position:absolute;left:0;width:100%;top:55px;font-family:"Arimo",sans-serif;font-size:23px}
.statement .claim{position:absolute;left:0;width:100%;top:92px;font-family:"Arimo",sans-serif;font-size:17.5px;line-height:20.5px}
.statement .claim em{font-style:normal;color:var(--gold)}
.statement .note{position:absolute;left:80px;width:218px;top:172px;font-size:7px;line-height:9px}

/* personas */
.persona-band{position:absolute;left:0;top:0;width:100%;height:116px;background:var(--blue)}
.persona-title{position:absolute;left:0;width:100%;top:44px;text-align:center;font-family:"Arimo",sans-serif;font-size:24px;color:var(--white)}
.persona-text{position:absolute;left:16px;width:346px;top:132px;text-align:center;font-size:7.4px;line-height:9.4px}
.persona-source{position:absolute;left:16px;top:190px;font-size:4.5px;color:var(--muted)}

.profile-card{position:absolute;background:var(--blue);color:var(--white)}
.profile-name{position:absolute;font-weight:700;font-size:11.5px}
.tiny{font-size:3.6px;line-height:5px}
.skill{position:absolute;font-size:3.8px}
.skill .bar{position:absolute;left:0;top:6px;height:1.6px}
.skill .pct{position:absolute;top:3px;font-size:3.6px}

.profile-list dt{font-weight:700;font-size:5.6px;margin-top:6px;color:var(--ink)}
.profile-list dt:first-child{margin-top:0}
.profile-list dd{font-size:4.6px;line-height:5.6px;color:var(--ink)}

.intro-gold{color:var(--gold)}
.text-col p{margin-top:4px}
.text-col p:first-child{margin-top:0}
</style>
</head>
<body>

<!-- Title slide -->
<section class="hero">
  <h1 class="hero-title">YOUR PITCH</h1>
  <div class="hero-rule"></div>
  <p class="hero-sub">NORTHVALE BASECAMP PHASE 7.4</p>
</section>

<!-- Feature checklist -->
<ul class="features">
  <li class="item" style="top:53px"><span class="box" style="top:3px"></span><span style="position:absolute;left:43px">Ratio 16:9</span></li>
  <li class="item" style="top:83px"><span class="box" style="top:3px"></span><span style="position:absolute;left:43px">Full HD</span></li>
  <li class="item" style="top:113px"><span class="box" style="top:3px"></span><span style="position:absolute;left:43px">Custom color pallet</span></li>
  <li class="item" style="top:143px"><span class="box" style="top:3px"></span><span style="position:absolute;left:43px">Custom Font -&nbsp; Easy Change</span></li>
  <li class="item" style="top:173px"><span class="box" style="top:3px"></span><span style="position:absolute;left:43px">Easy to edit, just drag and</span></li>
  <li class="item" style="top:204px"><span style="position:absolute;left:58px">drop images</span></li>
  <li class="item" style="top:234px"><span class="box" style="top:3px"></span><span style="position:absolute;left:43px">Can be included up to 40</span></li>
  <li class="item" style="top:261px"><span style="position:absolute;left:38px">slides;</span></li>
  <li class="item" style="top:291px"><span class="sq" style="top:10px"></span><span style="position:absolute;left:96px">Text + images (1,2,3,4)</span></li>
  <li class="item" style="top:321px"><span class="sq" style="top:10px"></span><span style="position:absolute;left:96px">Portfolio Slides</span></li>
  <li class="item" style="top:351px"><span class="sq" style="top:10px"></span><span style="position:absolute;left:96px">Text Slides</span></li>
  <li class="item" style="top:381px"><span class="sq" style="top:10px"></span><span style="position:absolute;left:96px">Data Slides</span></li>
  <li class="item" style="top:411px"><span class="box" style="top:3px"></span><span style="position:absolute;left:43px">In the sample load you will</span></li>
  <li class="item" style="top:438px"><span style="position:absolute;left:38px">find 22 slides</span></li>
</ul>

<!-- Row 1 -->
<section class="slide agenda" style="left:10px;top:512px">
  <div class="agenda-band"></div>
  <h2 class="agenda-title" style="left:29px">AGENDA</h2>
  <p class="agenda-label" style="left:20px"><b>Purpose</b> of<br>the “Pitch?”</p>
  <p class="agenda-label" style="left:97px"><b>Why</b> it’s<br>important</p>
  <p class="agenda-label" style="left:169px"><b>Styles</b> of<br>Pitches</p>
  <p class="agenda-label" style="left:239px"><b>Whom</b> do<br>you pitch to?</p>
  <p class="agenda-label" style="left:313px"><b>Build</b><br>your pitch</p>
  <div class="agenda-line" style="left:18px;width:352px"></div>
  <div class="agenda-dot" style="left:29px"><svg width="18" height="18" viewBox="0 0 18 18" fill="none" stroke="#fff" stroke-width="1.3"><circle cx="9" cy="9" r="7"/><circle cx="9" cy="9" r="4"/><circle cx="9" cy="9" r="1.2" fill="#fff"/></svg></div>
  <div class="agenda-dot" style="left:100px"><svg width="18" height="18" viewBox="0 0 18 18" fill="none" stroke="#fff" stroke-width="1.3"><circle cx="9" cy="10" r="6.5"/><path d="M9 6.5v7M11 8c-.5-1-3.5-1-3.5.5S11 9.8 11 11.3 8 13 7 12"/></svg></div>
  <div class="agenda-dot" style="left:171px"><svg width="18" height="18" viewBox="0 0 18 18" fill="none" stroke="#fff" stroke-width="1.3"><path d="M3 3l4 4M3 3h3M3 3v3M15 15l-4-4M15 15h-3M15 15v-3M15 3l-4 4M15 3h-3M15 3v3M3 15l4-4M3 15h3M3 15v-3"/></svg></div>
  <div class="agenda-dot" style="left:243px"><svg width="18" height="18" viewBox="0 0 18 18" fill="none" stroke="#fff" stroke-width="1.3"><circle cx="6" cy="6" r="2.2"/><circle cx="12" cy="6" r="2.2"/><path d="M2 14c0-3 2-4.5 4-4.5s4 1.5 4 4.5M8 14c0-3 2-4.5 4-4.5s4 1.5 4 4.5"/></svg></div>
  <div class="agenda-dot" style="left:315px"><svg width="18" height="18" viewBox="0 0 18 18" fill="none" stroke="#fff" stroke-width="1.3"><path d="M4 14l8-8M12 6l2-2 1 1-2 2zM14 14L6 6M6 6L3 4l1-1 2 3"/></svg></div>
  <p class="foot">Northvale LLC</p><span class="pageno">3</span>
</section>

<section class="slide agenda" style="left:412px;top:512px">
  <div class="agenda-band"></div>
  <h2 class="agenda-title" style="left:152px">AGENDA</h2>
  <p class="agenda-label" style="left:41px"><b>Deliver</b><br>your pitch</p>
  <p class="agenda-label" style="left:118px">Your next<br><b>meeting</b></p>
  <p class="agenda-label" style="left:201px"><b>Objection</b><br><b>Handling</b></p>
  <p class="agenda-label" style="left:274px"><b>“Secrets”</b><br>of Selling</p>
  <div class="agenda-line" style="left:20px;width:340px"></div>
  <div class="agenda-dot" style="left:47px"><svg width="18" height="18" viewBox="0 0 18 18" fill="none" stroke="#fff" stroke-width="1.3"><circle cx="9" cy="5" r="2.2"/><path d="M3 11h12M5 11v4M13 11v4M6 11c0-2 1.3-3.5 3-3.5s3 1.5 3 3.5"/></svg></div>
  <div class="agenda-dot" style="left:125px"><svg width="18" height="18" viewBox="0 0 18 18" fill="none" stroke="#fff" stroke-width="1.3"><rect x="3" y="4" width="12" height="11" rx="1"/><path d="M3 7h12M6 2.5v3M12 2.5v3"/><text x="9" y="13.5" font-size="5" fill="#fff" stroke="none" text-anchor="middle" font-family="Open Sans,sans-serif">12</text></svg></div>
  <div class="agenda-dot" style="left:202px"><svg width="18" height="18" viewBox="0 0 18 18" fill="none" stroke="#fff" stroke-width="1.3"><path d="M6 15V5.5a1 1 0 0 1 2 0V9M8 9V4a1 1 0 0 1 2 0v5M10 9V4.5a1 1 0 0 1 2 0V10M12 10V6.5a1 1 0 0 1 2 0V12c0 2-1.5 3-3.5 3H6"/></svg></div>
  <div class="agenda-dot" style="left:279px"><svg width="18" height="18" viewBox="0 0 18 18" fill="none" stroke="#fff" stroke-width="1.3"><circle cx="8" cy="7" r="2.5"/><path d="M3 15c0-3 2.2-4.5 5-4.5s5 1.5 5 4.5M12 4l3-2M13 6.5h3"/></svg></div>
  <p class="foot">Northvale LLC</p>
</section>

<section class="slide" style="left:810px;top:512px">
  <div class="abs" style="left:282px;top:0;width:96px;height:213px;background:var(--gold)"></div>
  <div class="abs" style="left:0;top:26px;width:3px;height:160px;background:var(--gold)"></div>
  <p class="brand" style="left:19px"><i></i>Northvale</p>
  <h3 class="heading" style="left:28px;top:66px;font-size:24px">To get them<br>wanting more</h3>
  <p class="body" style="left:28px;top:134px;width:172px">Don’t bore them with technical details about your product. I’ve heard many investors say that if they walk away from meeting and can’t remember anything. If this happens to you, then you’ve failed.</p>
  <div class="photo round" style="left:205px;top:28px;width:156px;height:156px;background:radial-gradient(circle at 45% 40%,#f4f1ec,#cfc7bc 60%,#7a6b5c)" role="img" aria-label="Photo: a small dog peeking over a table with a snack bowl and coffee"></div>
  <p class="foot" style="left:95px">Northvale LLC</p>
</section>

<!-- Row 2 -->
<section class="slide" style="left:10px;top:755px">
  <div class="abs" style="left:0;top:0;width:98px;height:213px;background:var(--gold)"></div>
  <div class="abs" style="left:375px;top:26px;width:3px;height:141px;background:var(--gold)"></div>
  <p class="brand" style="left:321px"><i></i>Northvale</p>
  <div class="photo round" style="left:20px;top:29px;width:155px;height:155px;background:radial-gradient(circle at 55% 50%,#e8e4dc,#a67c62 55%,#5a3d2e)" role="img" aria-label="Photo: hands holding a film clapperboard"></div>
  <h3 class="heading" style="left:186px;top:72px;font-size:23px">With the goal<br>to Take Action</h3>
  <p class="body" style="left:186px;top:133px;width:175px">Connecting the dots between a prospective clients need for pain relief to your solution to makes that pain go away.</p>
  <p class="foot">Northvale LLC</p>
</section>

<section class="slide statement" style="left:412px;top:755px">
  <p class="lead">For YOUR Profession</p>
  <p class="claim">Your pitch is the <em>TECHNIQUE</em><br>to get someone to consider<br>you to solve their problem</p>
  <p class="note">We rarely have the opportunity to pitch for investment in our business.</p>
</section>

<section class="slide" style="left:810px;top:755px;background:var(--gold)">
  <div class="photo" style="left:0;top:0;width:190px;height:213px;background:radial-gradient(ellipse at 55% 45%,#b9c3cc 0,#5d6a74 28%,#1e2429 62%,#0d1013)" role="img" aria-label="Photo: a presenter on stage before a large screen and audience"></div>
  <p class="abs" style="left:201px;top:72px;font-family:'Arimo',sans-serif;font-size:27px;line-height:35px;color:var(--white);white-space:nowrap">The Styles of<br>Pitches</p>
</section>

<!-- Row 3 -->
<section class="slide" style="left:10px;top:998px">
  <div class="abs" style="left:0;top:0;width:98px;height:213px;background:var(--gold)"></div>
  <div class="photo" style="left:15px;top:22px;width:167px;height:167px;background:linear-gradient(120deg,#cbbfb2,#efece8 45%,#9c8d80)" role="img" aria-label="Photo: hands holding an e-reader"></div>
  <p class="brand" style="left:321px"><i></i>Northvale</p>
  <h3 class="heading" style="left:188px;top:42px;font-size:24px;line-height:28px">Do so by<br>telling them a<br>story</h3>
  <p class="body" style="left:189px;top:134px;width:175px">Purpose is to show you’re relatable.&nbsp; Connect with your audience.&nbsp; It’s most effective when it connects emotionally.</p>
  <p class="foot">Northvale LLC</p>
</section>

<section class="slide" style="left:412px;top:998px">
  <div class="abs" style="left:280px;top:0;width:98px;height:213px;background:var(--gold)"></div>
  <p class="brand" style="left:19px"><i></i>Northvale</p>
  <h3 class="heading" style="left:18px;top:37px;font-size:19px;line-height:22.5px">Enhance your<br>story with<br>enthusiasm and<br>confidence</h3>
  <p class="body" style="left:19px;top:134px;width:170px;font-size:6.6px">People buy (or invest) in those who really want to help the customer.&nbsp; You don’t need to gush like a sports caster; nor should you act cheesy, like a used car salesman; nor should you act like you can’t be bothered.</p>
  <div class="photo" style="left:196px;top:22px;width:167px;height:167px;background:linear-gradient(180deg,#2a1d55 0,#6b2f7a 35%,#d8457a 62%,#3a2140 80%,#140c1c)" role="img" aria-label="Photo: silhouette of a person with raised arms against a purple sunset sky"></div>
  <p class="foot">Northvale LLC</p>
</section>

<section class="slide" style="left:810px;top:998px">
  <div class="abs" style="left:282px;top:0;width:96px;height:213px;background:var(--blue)"></div>
  <div class="abs" style="left:0;top:30px;width:3px;height:160px;background:var(--blue)"></div>
  <p class="brand" style="left:19px"><i></i>Northvale</p>
  <h3 class="heading" style="left:28px;top:72px;font-size:24px">The “video<br>pitch”</h3>
  <div class="photo round" style="left:205px;top:28px;width:156px;height:156px;background:radial-gradient(circle at 40% 35%,#5b4a3c,#2a2320 45%,#b7692a 80%,#e0a15a)" role="img" aria-label="Photo: a video camera filming in a library"></div>
  <p class="foot" style="left:95px">Northvale LLC</p>
</section>

<!-- Row 4 -->
<section class="slide" style="left:10px;top:1240px">
  <div class="abs" style="left:0;top:0;width:98px;height:213px;background:var(--blue)"></div>
  <div class="abs" style="left:375px;top:28px;width:3px;height:160px;background:var(--blue)"></div>
  <p class="brand" style="left:321px"><i></i>Northvale</p>
  <div class="photo round" style="left:20px;top:29px;width:155px;height:155px;background:radial-gradient(circle at 50% 55%,#6a5436,#c9a866 40%,#3b2e1f 75%,#1d1710)" role="img" aria-label="Photo: a brass elevator floor-indicator dial"></div>
  <h3 class="heading" style="left:186px;top:69px;font-size:24px">The “elevator<br>pitch”</h3>
  <p class="body" style="left:186px;top:134px;width:175px">Don’t bore them with technical details about your product. I’ve heard many investors say that if they walk away from meeting and can’t remember anything. If this happens to you, then you’ve failed.</p>
  <p class="foot">Northvale LLC</p>
</section>

<section class="slide" style="left:412px;top:1240px">
  <p class="slide-title">Customer Journey Map</p>
  <p class="brand" style="left:323px"><i></i>Northvale</p>
  <svg class="abs" style="left:0;top:0" width="378" height="213" viewBox="0 0 378 213" font-family="Open Sans,sans-serif">
    <g fill="#f5b300">
      <polygon points="104,37 151,37 155,41.5 151,46 104,46 108,41.5"/>
      <polygon points="155,37 202,37 206,41.5 202,46 155,46 159,41.5"/>
      <polygon points="206,37 253,37 257,41.5 253,46 206,46 210,41.5"/>
      <polygon points="257,37 304,37 308,41.5 304,46 257,46 261,41.5"/>
      <rect x="71" y="51" width="31" height="13"/>
      <polygon points="104,51 151,51 155,57.5 151,64 104,64 108,57.5"/>
      <polygon points="155,51 202,51 206,57.5 202,64 155,64 159,57.5"/>
      <polygon points="206,51 253,51 257,57.5 253,64 206,64 210,57.5"/>
      <polygon points="257,51 304,51 308,57.5 304,64 257,64 261,57.5"/>
      <rect x="71" y="79" width="31" height="39"/>
      <rect x="71" y="121" width="31" height="28"/>
      <rect x="71" y="160" width="31" height="18"/>
      <rect x="71" y="181" width="31" height="21"/>
    </g>
    <g fill="#fff" font-size="3.6" text-anchor="middle">
      <text x="130" y="43">CONSIDER</text><text x="181" y="43">EVALUATE</text><text x="232" y="43">BUY</text><text x="283" y="43">ENJOY</text>
      <text x="130" y="59">VISIT WEBSITE</text><text x="181" y="59">REGISTER</text><text x="232" y="59">ONBOARD</text><text x="283" y="57">CONVERT &amp;</text><text x="283" y="61.5">RETAIN</text>
    </g>
    <g fill="#333" font-size="3.4" font-weight="700" text-anchor="middle">
      <text x="86.5" y="57">LIFECYCLE</text><text x="86.5" y="61">STAGE</text>
      <text x="86.5" y="95">TOUCH</text><text x="86.5" y="99">POINTS &amp;</text><text x="86.5" y="103">SCORECARD</text>
      <text x="86.5" y="137">CHALLENGES</text>
      <text x="86.5" y="170.5">METRICS</text>
      <text x="86.5" y="190">Improvement</text><text x="86.5" y="194">Opportunities</text>
    </g>
    <g fill="#333" font-size="3.4" font-weight="700">
      <text x="71" y="75">USER EXPERIENCE</text>
      <text x="71" y="157">RECOMMENDATION</text>
    </g>
    <g stroke="#999" stroke-width=".4"><line x1="71" y1="76.5" x2="308" y2="76.5"/><line x1="71" y1="158.5" x2="308" y2="158.5"/></g>
    <g fill="#2b74a6">
      <polygon points="104,79 150,79 155,98.5 150,118 104,118 109,98.5"/>
      <polygon points="155,79 201,79 206,98.5 201,118 155,118 160,98.5"/>
      <polygon points="206,79 252,79 257,98.5 252,118 206,118 211,98.5"/>
      <polygon points="257,79 303,79 308,98.5 303,118 257,118 262,98.5"/>
      <rect x="104" y="121" width="49" height="28"/><rect x="155" y="121" width="49" height="28"/><rect x="206" y="121" width="49" height="28"/><rect x="257" y="121" width="49" height="28"/>
      <rect x="104" y="160" width="49" height="18"/><rect x="155" y="160" width="49" height="18"/><rect x="206" y="160" width="49" height="18"/><rect x="257" y="160" width="49" height="18"/>
      <rect x="104" y="181" width="49" height="21"/><rect x="155" y="181" width="49" height="21"/><rect x="206" y="181" width="49" height="21"/><rect x="257" y="181" width="49" height="21"/>
    </g>
    <g fill="#f5b300"><circle cx="114" cy="88" r="1.2"/><circle cx="114" cy="95" r="1.2"/><circle cx="114" cy="102" r="1.2"/><circle cx="165" cy="92" r="1.2"/><circle cx="165" cy="100" r="1.2"/><circle cx="216" cy="88" r="1.2"/><circle cx="216" cy="95" r="1.2"/><circle cx="216" cy="102" r="1.2"/><circle cx="216" cy="109" r="1.2"/><circle cx="267" cy="88" r="1.2"/><circle cx="267" cy="95" r="1.2"/><circle cx="267" cy="102" r="1.2"/><circle cx="267" cy="109" r="1.2"/></g>
    <g fill="#fff" font-size="3.2">
      <text x="117" y="89">Site design</text><text x="117" y="96">Messaging</text><text x="117" y="103">Content</text>
      <text x="168" y="93">Call-to-action</text><text x="168" y="101">Sign-up form</text>
      <text x="219" y="89">Tool tips</text><text x="219" y="96">Self-serve</text><text x="219" y="103">Integrations</text><text x="219" y="110">Docs</text>
      <text x="270" y="89">Nurture emails</text><text x="270" y="96">Payment steps</text><text x="270" y="103">Calls-to-action</text><text x="270" y="110">Pricing &amp; offers</text>
      <text x="107" y="130">Unclear messaging</text><text x="107" y="135">Weak content</text>
      <text x="158" y="130">Unclear CTAs</text><text x="158" y="135">Long sign-up form</text>
      <text x="209" y="130">Slow first steps</text><text x="209" y="135">Thin docs</text>
      <text x="260" y="130">Few upsell emails</text><text x="260" y="135">Vague pricing</text>
      <text x="107" y="168">Bounce rate</text><text x="107" y="173">Time on page</text>
      <text x="158" y="170.5">Sign-up rate by channel</text>
      <text x="209" y="168">Active users</text><text x="209" y="173">Setup completion</text>
      <text x="260" y="168">Churn &amp; LTV</text><text x="260" y="173">Upgrade rate</text>
      <text x="107" y="189">Clear copy</text><text x="107" y="194">Better visuals</text>
      <text x="158" y="189">Fewer form fields</text><text x="158" y="194">Bold CTA button</text>
      <text x="209" y="189">Guided setup</text><text x="209" y="194">Welcome emails</text>
      <text x="260" y="189">Timely offers</text><text x="260" y="194">Clear price tiers</text>
    </g>
  </svg>
</section>

<section class="slide" style="left:810px;top:1240px">
  <div class="persona-band"></div>
  <h3 class="persona-title">B2C PERSONAS</h3>
  <p class="persona-text">A buyer persona is a semi-fictional representation of one of your ideal clients based on real data (your research). We’re looking for common behavior patterns, shared pain points and where they hang out.&nbsp; You will know what are their pain points, their goals, and where they hang out. So you can offer them the right solutions and promote to them in language that they understand.</p>
  <p class="persona-source">- Leadwise</p>
  <p class="foot">Northvale LLC</p>
</section>

<!-- Row 5 -->
<section class="slide" style="left:10px;top:1484px">
  <div class="photo" style="left:190px;top:26px;width:156px;height:160px;background:linear-gradient(90deg,#e9e9e9,#d2cdc8 55%,#8a6d5a 70%,#ececec)" role="img" aria-label="Photo: a woman with curly hair holding a pen, smiling"></div>
  <div class="profile-card" style="left:32px;top:43px;width:187px;height:130px">
    <p class="profile-name" style="left:12px;top:9px">MARA ELLIS</p>
    <ul class="abs tiny" style="left:14px;top:33px;width:110px;list-style:disc">
      <li>Studies late, but goes to early classes</li>
      <li>Takes the train to work each day</li>
      <li>Has a cat and a strong sense of duty</li>
      <li>Works part-time at a coffee shop</li>
      <li>Shares a flat with a friend</li>
      <li>Spends a lot of time online</li>
    </ul>
    <div class="skill" style="left:12px;top:77px;width:150px">Branding<span class="bar" style="width:115px;background:var(--gold)"></span><span class="pct" style="left:126px">100%</span></div>
    <div class="skill" style="left:12px;top:89px;width:150px">Public Relations<span class="bar" style="width:92px;background:var(--gold)"></span><span class="pct" style="left:106px">80%</span></div>
    <div class="skill" style="left:12px;top:101px;width:150px">Graphic Design<span class="bar" style="width:69px;background:var(--white)"></span><span class="pct" style="left:84px">60%</span></div>
    <div class="skill" style="left:12px;top:113px;width:150px">Social Marketing<span class="bar" style="width:98px;background:var(--white)"></span><span class="pct" style="left:112px">85%</span></div>
  </div>
</section>

<section class="slide" style="left:412px;top:1484px">
  <div class="abs" style="left:0;top:0;width:119px;height:213px;background:var(--blue)"></div>
  <div class="photo" style="left:47px;top:75px;width:87px;height:87px;background:radial-gradient(circle at 50% 45%,#b58d74,#6b5244 45%,#2c2623)" role="img" aria-label="Photo: portrait of a thoughtful grey-haired man in glasses"></div>
  <p class="abs" style="left:182px;top:24px;font-weight:700;font-size:10.5px;color:#4f6f87">OWEN PRYCE</p>
  <p class="abs tiny" style="left:182px;top:40px;width:150px;color:var(--muted);text-align:justify">Owen is VP of Claims at a large health insurer. He has been at the company for one year and has assessed the team, compared rivals and found his unit is behind. He wants to modernize how claims are handled, deploy new tools and cut costs before the year is out.</p>
  <p class="abs tiny" style="left:182px;top:86px;width:150px;color:var(--ink)">AGE: 47<br>TITLE: Vice President<br>FAMILY: Married, 3 kids<br>LOCATION: Lakeview, MN<br>ARCHETYPE: Decision maker who<br>drives change and likes proof<br>EDUCATION: MBA<br>INCOME: $95,000</p>
  <div class="skill" style="left:182px;top:148px;width:160px;color:var(--muted)">Branding<span class="bar" style="width:125px;background:var(--orange)"></span><span class="pct" style="left:130px">100%</span></div>
  <div class="skill" style="left:182px;top:160px;width:160px;color:var(--muted)">Public Relations<span class="bar" style="width:100px;background:var(--orange)"></span><span class="pct" style="left:105px">80%</span></div>
  <div class="skill" style="left:182px;top:172px;width:160px;color:var(--muted)">Graphic Design<span class="bar" style="width:75px;background:#5d5d5d"></span><span class="pct" style="left:80px">60%</span></div>
  <div class="skill" style="left:182px;top:184px;width:160px;color:var(--muted)">Social Marketing<span class="bar" style="width:106px;background:#5d5d5d"></span><span class="pct" style="left:111px">85%</span></div>
</section>

<section class="slide" style="left:810px;top:1484px">
  <p class="slide-title strong" style="left:21px;top:13px">Route map</p>
  <p class="brand" style="left:323px"><i></i>Northvale</p>
  <svg class="abs" style="left:0;top:0" width="378" height="213" viewBox="0 0 378 213" font-family="Open Sans,sans-serif">
    <rect x="87" y="54" width="66" height="22" fill="#f5b300"/>
    <rect x="153" y="54" width="66" height="22" fill="#2b74a6"/>
    <rect x="219" y="54" width="65" height="22" fill="#f39c33"/>
    <rect x="284" y="54" width="66" height="22" fill="#5d5d5d"/>
    <g fill="#fff" font-size="7" text-anchor="middle"><text x="120" y="67.5">Concept</text><text x="186" y="67.5">Prototype</text><text x="251.5" y="67.5">Develop</text><text x="317" y="67.5">Task End</text></g>
    <text x="34" y="67.5" font-size="5.5" fill="#555">President</text>
    <g fill="#d9d9d9"><rect x="34" y="78" width="316" height="15"/><rect x="34" y="112" width="316" height="15"/><rect x="34" y="146" width="316" height="15"/></g>
    <g fill="#ececec"><rect x="34" y="95" width="316" height="15"/><rect x="34" y="129" width="316" height="15"/></g>
    <g font-size="5" fill="#555"><text x="36" y="87.5">Marketing</text><text x="36" y="104.5">Desing</text><text x="36" y="121.5">Manufacture</text><text x="36" y="138.5">Finance</text><text x="36" y="155.5">Laboratory</text></g>
    <defs>
      <g id="tick"><path d="M-2.4 0l1.7 1.7L2.6-1.7" fill="none" stroke="#fff" stroke-width="1"/></g>
      <g id="cross"><path d="M-1.8-1.8l3.6 3.6M1.8-1.8l-3.6 3.6" fill="none" stroke="#fff" stroke-width="1"/></g>
    </defs>
    <g>
      <circle cx="120" cy="85.5" r="5" fill="#f5b300"/><use href="#tick" x="120" y="85.5"/>
      <circle cx="186" cy="85.5" r="5" fill="#2b74a6"/><use href="#tick" x="186" y="85.5"/>
      <circle cx="251.5" cy="85.5" r="5" fill="#f39c33"/><use href="#cross" x="251.5" y="85.5"/>
      <circle cx="317" cy="85.5" r="5" fill="#5d5d5d"/><use href="#tick" x="317" y="85.5"/>
      <circle cx="186" cy="102.5" r="5" fill="#2b74a6"/><use href="#tick" x="186" y="102.5"/>
      <circle cx="251.5" cy="102.5" r="5" fill="#f39c33"/><use href="#tick" x="251.5" y="102.5"/>
      <circle cx="317" cy="102.5" r="5" fill="#5d5d5d"/><use href="#tick" x="317" y="102.5"/>
      <circle cx="120" cy="119.5" r="5" fill="#f39c33"/><use href="#cross" x="120" y="119.5"/>
      <circle cx="317" cy="119.5" r="5" fill="#5d5d5d"/><use href="#tick" x="317" y="119.5"/>
      <circle cx="186" cy="136.5" r="5" fill="#2b74a6"/><use href="#tick" x="186" y="136.5"/>
      <circle cx="317" cy="136.5" r="5" fill="#5d5d5d"/><use href="#tick" x="317" y="136.5"/>
      <circle cx="251.5" cy="153.5" r="5" fill="#f39c33"/><use href="#tick" x="251.5" y="153.5"/>
      <circle cx="317" cy="153.5" r="5" fill="#5d5d5d"/><use href="#tick" x="317" y="153.5"/>
    </g>
  </svg>
  <p class="foot" style="font-size:3.5px">Northvale LLC</p><span class="pageno" style="font-size:3.5px">13</span>
</section>

<!-- Row 6 -->
<section class="slide" style="left:10px;top:1726px">
  <p class="slide-title strong">Project Develop</p>
  <p class="brand" style="left:323px"><i></i>Northvale</p>
  <p class="abs tiny" style="left:31px;top:24px;width:325px;color:var(--muted)">Plan each phase of the project here, showing how the work flows from start to finish across the year. Adjust the bars to match real dates and owners for every task.</p>
  <svg class="abs" style="left:0;top:0" width="378" height="213" viewBox="0 0 378 213" font-family="Open Sans,sans-serif">
    <rect x="30" y="47" width="319" height="10" fill="#7a7a7a"/>
    <rect x="30" y="57" width="37" height="130" fill="#bdbdbd"/>
    <g stroke="#d6d6d6" stroke-width=".4">
      <path d="M67 57v130M76.1 57v130M85.2 57v130M94.3 57v130M103.4 57v130M112.5 57v130M121.6 57v130M130.7 57v130M139.8 57v130M148.9 57v130M158 57v130M167.1 57v130M176.2 57v130M185.3 57v130M194.4 57v130M203.5 57v130M212.6 57v130M221.7 57v130M230.8 57v130M239.9 57v130M249 57v130M258.1 57v130M267.2 57v130M276.3 57v130M285.4 57v130M294.5 57v130M303.6 57v130M312.7 57v130M321.8 57v130M330.9 57v130M340 57v130M349 57v130"/>
      <path d="M30 67.8h319M30 78.6h319M30 89.5h319M30 100.3h319M30 111.1h319M30 122h319M30 132.8h319M30 143.6h319M30 154.5h319M30 165.3h319M30 176.1h319M30 187h319"/>
    </g>
    <g fill="#fff" font-size="3.6" text-anchor="middle">
      <text x="48" y="53.5">2019</text>
      <text x="71.5" y="53.5">1</text><text x="80.6" y="53.5">2</text><text x="89.7" y="53.5">3</text><text x="98.8" y="53.5">4</text><text x="107.9" y="53.5">5</text><text x="117" y="53.5">6</text><text x="126.1" y="53.5">7</text><text x="135.2" y="53.5">8</text><text x="144.3" y="53.5">9</text><text x="153.4" y="53.5">10</text><text x="162.5" y="53.5">11</text><text x="171.6" y="53.5">12</text><text x="180.7" y="53.5">13</text><text x="189.8" y="53.5">14</text><text x="198.9" y="53.5">15</text><text x="208" y="53.5">16</text><text x="217.1" y="53.5">17</text><text x="226.2" y="53.5">18</text><text x="235.3" y="53.5">19</text><text x="244.4" y="53.5">20</text><text x="253.5" y="53.5">21</text><text x="262.6" y="53.5">22</text><text x="271.7" y="53.5">23</text><text x="280.8" y="53.5">24</text><text x="289.9" y="53.5">25</text><text x="299" y="53.5">26</text><text x="308.1" y="53.5">27</text><text x="317.2" y="53.5">28</text><text x="326.3" y="53.5">29</text><text x="335.4" y="53.5">30</text><text x="344.5" y="53.5">31</text>
    </g>
    <g fill="#fff" font-size="3.8">
      <text x="33" y="64">Jan</text><text x="33" y="74.8">Feb</text><text x="33" y="85.6">Mar</text><text x="33" y="96.5">Apr</text><text x="33" y="107.3">May</text><text x="33" y="118.1">Jun</text><text x="33" y="129">Jul</text><text x="33" y="139.8">Ago</text><text x="33" y="150.6">Sep</text><text x="33" y="161.5">Oct</text><text x="33" y="172.3">Nov</text><text x="33" y="183.1">Dic</text>
    </g>
    <rect x="61" y="59.5" width="125" height="6.5" fill="#f5b300"/>
    <rect x="160" y="70.3" width="107" height="6.5" fill="#2b74a6"/>
    <rect x="75" y="91.9" width="237" height="6.5" fill="#f39c33"/>
    <rect x="189" y="113.6" width="160" height="6.5" fill="#6d6d6d"/>
    <rect x="94" y="146.1" width="64" height="6.5" fill="#f39c33"/>
    <rect x="170" y="167.8" width="141" height="6.5" fill="#6d6d6d"/>
    <g fill="#fff" font-size="3.6" text-anchor="middle"><text x="123.5" y="64">Text</text><text x="213.5" y="74.8">Text</text><text x="193.5" y="96.4">Text</text><text x="269" y="118.1">Text</text><text x="126" y="150.6">Text</text><text x="240.5" y="172.3">Text</text></g>
  </svg>
  <p class="foot" style="font-size:3.5px">Northvale LLC</p><span class="pageno" style="font-size:3.5px">12</span>
</section>

<section class="slide" style="left:412px;top:1726px">
  <p class="slide-title strong">Schedule</p>
  <p class="brand" style="left:323px"><i></i>Northvale</p>
  <svg class="abs" style="left:0;top:0" width="378" height="213" viewBox="0 0 378 213" font-family="Open Sans,sans-serif">
    <rect x="36" y="33" width="307" height="9" fill="#bdbdbd"/>
    <rect x="36" y="42" width="307" height="8" fill="#d4d4d4"/>
    <g fill="#fff" font-size="3.8"><text x="39" y="39.5">Month</text></g>
    <g fill="#fff" font-size="3.6"><text x="39" y="47.5">SUNDAY</text><text x="90" y="47.5">MONDAY</text><text x="141" y="47.5">TUESDAY</text><text x="192" y="47.5">WEDNESDAY</text><text x="243" y="47.5">THURSDAY</text><text x="294" y="47.5">FRIDAY</text><text x="320" y="47.5">SATURDAY</text></g>
    <g fill="none" stroke="#e0c27a" stroke-width=".5">
      <rect x="36" y="50" width="307" height="141"/>
      <path d="M87 50v141M138 50v141M189 50v141M240 50v141M291 50v141M317 50v141M36 78h307M36 106h307M36 134h307M36 162h307"/>
    </g>
    <g fill="#555" font-size="3.8">
      <text x="39" y="55.5">1</text><text x="90" y="55.5">2</text><text x="141" y="55.5">3</text><text x="192" y="55.5">4</text><text x="243" y="55.5">5</text><text x="294" y="55.5">6</text><text x="320" y="55.5">7</text>
      <text x="39" y="83.5">8</text><text x="90" y="83.5">9</text><text x="141" y="83.5">10</text><text x="192" y="83.5">11</text><text x="243" y="83.5">12</text><text x="294" y="83.5">13</text><text x="320" y="83.5">14</text>
      <text x="39" y="111.5">15</text><text x="90" y="111.5">16</text><text x="141" y="111.5">17</text><text x="192" y="111.5">18</text><text x="243" y="111.5">19</text><text x="294" y="111.5">20</text><text x="320" y="111.5">21</text>
      <text x="39" y="139.5">22</text><text x="90" y="139.5">23</text><text x="141" y="139.5">24</text><text x="192" y="139.5">25</text><text x="243" y="139.5">26</text><text x="294" y="139.5">27</text><text x="320" y="139.5">28</text>
      <text x="39" y="167.5">29</text><text x="90" y="167.5">30</text>
    </g>
    <rect x="36" y="58" width="281" height="11" fill="#d9a400"/>
    <rect x="87" y="86" width="51" height="11" fill="#2b74a6"/><rect x="138" y="86" width="51" height="11" fill="#2b74a6"/>
    <rect x="138" y="114" width="179" height="11" fill="#f39c33"/>
    <rect x="87" y="142" width="230" height="11" fill="#6d6d6d"/>
    <rect x="36" y="170" width="102" height="11" fill="#e07b1a"/>
    <g fill="#fff" font-size="3.8">
      <text x="39" y="65">Text</text><text x="294" y="65">Texto</text>
      <text x="90" y="93">Texto</text><text x="141" y="93">Texto</text>
      <text x="141" y="121">Text</text><text x="294" y="121">Text</text>
      <text x="90" y="149">Text</text><text x="294" y="149">Text</text>
      <text x="39" y="177">Text</text><text x="90" y="177">Text</text>
    </g>
  </svg>
  <p class="foot" style="font-size:3.5px">Northvale LLC</p><span class="pageno" style="font-size:3.5px">14</span>
</section>

<section class="slide" style="left:810px;top:1726px">
  <p class="slide-title" style="left:21px;top:12px">Common buyer profiles</p>
  <p class="brand" style="left:323px"><i></i>Northvale</p>
  <div class="photo round" style="left:21px;top:33px;width:148px;height:148px;background:linear-gradient(180deg,#e9f4f7 0,#cfe8ee 55%,#1e8aa0 72%,#13657a)" role="img" aria-label="Illustration: a team seated at a table beneath a network of connected ideas"></div>
  <dl class="abs profile-list" style="left:196px;top:33px;width:165px">
    <dt>The User</dt><dd>the person who will use your service. In small organizations, not only is someone a User but also they are the Approver and Evaluator</dd>
    <dt>The Evaluator</dt><dd>anyone who evaluates the purchase from an operational, financial, technical, or legal perspective</dd>
    <dt>The Decision Maker</dt><dd>the person(s) in the sale who, should they bless the opportunity or you, the odds of your winning will significantly increase.</dd>
    <dt>The Approver</dt><dd>The Approver makes the final “yes” or “no” decision based on criteria that align with the strategic goals of his problems.</dd>
    <dt>The Champion/Mentor/Neutral/Enemy</dt><dd>Any one of the four roles noted above can have one of these “statuses.”</dd>
  </dl>
  <p class="foot" style="font-size:3.5px">Northvale LLC</p><span class="pageno" style="font-size:3.5px">16</span>
</section>

<!-- Row 7 -->
<section class="slide" style="left:10px;top:1969px">
  <p class="slide-title">Buying process</p>
  <p class="brand" style="left:323px"><i></i>Northvale</p>
  <div class="photo" style="left:54px;top:34px;width:85px;height:141px;background:linear-gradient(180deg,#eef3f8,#dce7f1 50%,#eef3f8)" role="img" aria-label="Illustration: business figures with a megaphone, a presentation and a handshake, linked by arrows"></div>
  <div class="abs text-col" style="left:192px;top:38px;width:170px;font-size:5.3px;line-height:6.6px">
    <p class="intro-gold">Identify the process this buyer persona will follow to explore and select the product, service or solution that can overcome the “perceived barriers” and achieve the “success factor(s).”</p>
    <p>These insights are best detailed in a table that begins with the business triggers that cause this buyer to commence a search for a solution, and ends with a satisfied reference customer (see step 2).</p>
    <p>At each step in the buying process, identify each of the buyer persona(s) who are critical to the decision to proceed to the next step, what role each plays, and the resources each consults to find answers to their questions.</p>
    <p>Note that this insight details the buyer’s process to arrive at a decision, not the selling process that sales people may have defined.</p>
  </div>
  <p class="foot" style="font-size:3.5px">Northvale LLC</p><span class="pageno" style="font-size:3.5px">17</span>
</section>

<section class="slide" style="left:412px;top:1969px">
  <p class="slide-title">DECISION CRITERIA</p>
  <p class="brand" style="left:323px"><i></i>Northvale</p>
  <div class="abs text-col" style="left:18px;top:36px;width:172px;font-size:5.3px;line-height:6.4px">
    <p class="intro-gold">As this buyer persona navigates the buying process, this insight specifies the aspects of the product, service, solution or company that they buyer will assess as they evaluate each of the alternative solutions.</p>
    <p>As insight into the “decision criteria” avoids jargon, ex. “easy-to-use,” or “scalable.” “Decision criteria” insights reveal details about the buyers’ expectations for the capabilities they consider most important, plus an explanation of how the buyer arrived at their conclusions.</p>
    <p>The “decision criteria” insights might specify, as an example, which aspects of the solution this person expected to be “easy-to-use” and how they determined that chosen solution is the easiest.</p>
    <p>For critical buyer personas, it is critical to include decision criteria insights from buyers who chose you as well as those who chose a competitor, plus those who chose to do nothing at all.</p>
  </div>
  <div class="photo round" style="left:200px;top:36px;width:160px;height:160px;background:radial-gradient(circle at 50% 45%,#8a9099,#5e646d 60%,#474c54)" role="img" aria-label="Illustration: a thinker surrounded by icons for travel, calendar, goals and ideas"></div>
  <p class="foot" style="font-size:3.5px">Northvale LLC</p><span class="pageno" style="font-size:3.5px">18</span>
</section>

<section class="slide" style="left:810px;top:1969px">
  <p class="slide-title">PERCEIVED BARRIERS</p>
  <p class="brand" style="left:323px"><i></i>Northvale</p>
  <div class="abs text-col" style="left:14px;top:44px;width:185px;font-size:5.6px;line-height:6.8px">
    <p class="intro-gold" style="margin-bottom:14px">This insight captures the buyers reasons to question whether your solution or company is capable of achieving the targeted “success factors.”</p>
    <p>The most useful part of this insight relates to the personal or business obstacles that this buyer sees as interfering with their chance for success.</p>
    <p>Other “perceived barriers” may result from this buyer’s persona’s prior experiences with your product or company or with other products or services similar to yours.</p>
    <p>Expect to gain insights into product or company specific “perceived barriers” that are no longer (or never were) actually correct.</p>
  </div>
  <div class="photo" style="left:215px;top:47px;width:145px;height:145px;border-radius:30px 30px 45% 45%;background:linear-gradient(180deg,#3c4268,#2c3155 60%,#2fb6e4 85%,#1d7fb0)" role="img" aria-label="Illustration: a pair of navy binoculars with blue lenses"></div>
  <p class="foot" style="font-size:3.5px">Northvale LLC</p><span class="pageno" style="font-size:3.5px">19</span>
</section>

</body>
</html>
```